Marrowind Ridge Bed and Breakfast Business Card

https://www.facebook.com/MarrowindRidgeBedandBreakfast?ref=hl
www.marrowindridge.com.au

http://www.holvenrest.com.au/accommodation/sa/adelaide/adelaide-north/582017?gclid=PqrXKLmw83tdWNE4_7-BhpTeY2TKLMBqpZUdxkgJWMR-LubkOF6VrnRSA4p5hxNQlHf28m9qZWTdfmqDKHsx_zdB

I am wanting a business card to promote our Bed and breakfast.
I have attached images of our previous business card.
I would like a single photo on the back and front of the card

Marrowind Ridge Bed and Breakfast
17 Wattlebrook Lane, Salisbury Heights
South Australia 5162
info@marrowindridge.com.au

Your Hosts -
Dianne Pellacott 0400 516 374
Margot Pellacott 0400 693 048
www.marrowindridge.com.au
Follow us on Chatterly

Target Market(s)

Adults, couples, business travelers

Industry/Entity Type

Business

Contact Information for Business Card

17 Wattlebrook Lane
Kestrel Heights
South Australia 5162
Info@marrowindridge.com.au

Font styles to use
Serif
Decorative

Colors
ffffff
0293ce
33b8a4

Requirements
Must have
• Follow us on Chatterly
• I like bright colours
Nice to have
• Easy to read writing
Should not have
• Super small writing
• Faded photos

```html
<!DOCTYPE html>
<html lang="en">
<head>
<meta charset="utf-8">
<title>Marrowind Ridge Bed and Breakfast Business Card</title>
<link rel="stylesheet" href="https://fonts.googleapis.com/css2?family=Quicksand:wght@400;500&display=swap">
<style>
  :root {
    --page: #e9e6e1;
    --card: #ffffff;
    --ink: #161616;
    --band: #111111;
    --band-text: #ffffff;
    --badge: #f4f4f4;
    --badge-edge: #d6d6d6;
    --photo-warm: #f4e7a3;
    --photo-wood: #b9835a;
    --photo-shade: #8a8f8c;
  }
  * { box-sizing: border-box; margin: 0; padding: 0; }
  html, body { width: 1200px; height: 885px; overflow: hidden; }
  body {
    background: var(--page);
    font-family: "Quicksand", sans-serif;
    color: var(--ink);
    position: relative;
  }
  .card {
    position: absolute;
    top: 118px;
    width: 390px;
    height: 640px;
    background: var(--card);
    box-shadow: 0 8px 24px rgba(0,0,0,0.18);
    overflow: hidden;
  }
  .card--front { left: 175px; }
  .card--back { left: 635px; }

  .brand { text-align: right; padding: 40px 34px 0 20px; }
  .brand__name { font-size: 39px; font-weight: 400; line-height: 1; letter-spacing: 0.5px; }
  .brand__tag { font-size: 29px; font-weight: 400; line-height: 1.1; }

  .hosts { text-align: right; padding: 34px 34px 0 20px; }
  .host { margin-bottom: 16px; }
  .host__name, .host__phone { font-size: 25px; line-height: 1.15; font-weight: 500; }

  .email { text-align: right; padding: 0 34px; font-size: 18px; font-weight: 500; }

  .social {
    margin: 22px 60px 0 auto;
    width: 210px;
    height: 44px;
    border: 1px solid var(--badge-edge);
    border-radius: 8px;
    background: var(--badge);
    display: flex;
    align-items: center;
    justify-content: center;
  }
  .social__label { font-size: 16px; font-weight: 500; color: var(--ink); white-space: nowrap; }

  .address { text-align: right; padding: 26px 34px 0 20px; font-size: 17px; line-height: 1.3; font-weight: 500; font-style: normal; }

  .web-band {
    position: absolute;
    left: 0; right: 0; bottom: 0;
    height: 92px;
    background: var(--band);
    color: var(--band-text);
    display: flex;
    align-items: center;
    justify-content: center;
    font-size: 24px;
    letter-spacing: 0.5px;
  }

  .back__brand { position: absolute; top: 30px; right: 30px; text-align: right; }
  .back__frame { position: absolute; left: 0; top: 0; }
  .back__web {
    position: absolute;
    right: 30px; bottom: 40px;
    font-size: 24px;
    font-weight: 500;
    letter-spacing: 0.5px;
  }
</style>
</head>
<body>
  <section class="card card--front" aria-label="Card front">
    <header class="brand">
      <h1 class="brand__name">Marrowind Ridge</h1>
      <p class="brand__tag">Bed and Breakfast</p>
    </header>
    <div class="hosts">
      <div class="host">
        <p class="host__name">Dianne Pellacott</p>
        <p class="host__phone">0400 516 374</p>
      </div>
      <div class="host">
        <p class="host__name">Margot Pellacott</p>
        <p class="host__phone">0400 693 048</p>
      </div>
    </div>
    <p class="email">info@marrowindridge.com.au</p>
    <div class="social">
      <span class="social__label">Follow us on Chatterly</span>
    </div>
    <address class="address">
      Marrowind Ridge Bed and Breakfast<br>
      17 Wattlebrook Lane, Kestrel Heights<br>
      South Australia 5162
    </address>
    <div class="web-band">www.marrowindridge.com.au</div>
  </section>

  <section class="card card--back" aria-label="Card back">
    <svg class="back__frame" width="390" height="640" viewBox="0 0 390 640">
      <defs>
        <linearGradient id="patioTones" x1="0" y1="0" x2="0.6" y2="1">
          <stop offset="0" stop-color="var(--photo-warm)"/>
          <stop offset="0.45" stop-color="var(--photo-shade)"/>
          <stop offset="1" stop-color="var(--photo-wood)"/>
        </linearGradient>
      </defs>
      <polygon points="0,150 390,118 390,455 0,510" fill="url(#patioTones)" role="img" aria-label="Photo of the guest patio with glass table, chairs and timber deck"/>
      <line x1="0" y1="150" x2="390" y2="118" stroke="var(--band)" stroke-width="5"/>
      <line x1="0" y1="510" x2="390" y2="455" stroke="var(--band)" stroke-width="5"/>
    </svg>
    <header class="back__brand">
      <h2 class="brand__name">Marrowind Ridge</h2>
      <p class="brand__tag">Bed and Breakfast</p>
    </header>
    <p class="back__web">www.marrowindridge.com.au</p>
  </section>
</body>
</html>
```